Business Card Design

we need a business card design and logo for a new cleaning company ,called brightwater cleaning Service,LLC .we provide cleaning services
Updates

i will also like to include the company's website in the business card   brightwatercleaningservice.example

Industry/Entity Type

Business

Contact Information for Business Card

Brightwater Cleaning Service,LLC
Marco Villanueva
Owner
marco@brightwatercleaningservice.example
Cell 555-318-7724
Office 555-374-6082

```html
<!DOCTYPE html>
<html lang="en">
<head>
<meta charset="utf-8">
<title>Brightwater Cleaning Service, LLC – Business Card</title>
<link rel="stylesheet" href="https://fonts.googleapis.com/css2?family=Open+Sans:wght@400;500&display=swap">
<style>
  :root {
    --card-top: #2a2b30;
    --card-glow: #55565e;
    --card-deep: #0b0c0e;
    --wave-dark: #101214;
    --rule: #f4f4f6;
    --ink: #ffffff;
    --ink-soft: #ececee;
  }
  html, body {
    margin: 0;
    padding: 0;
    width: 1200px;
    height: 702px;
    overflow: hidden;
    background: var(--card-deep);
  }
  .card {
    position: relative;
    width: 1200px;
    height: 702px;
    overflow: hidden;
    font-family: "Open Sans", sans-serif;
    color: var(--ink);
  }
  .card-backdrop {
    position: absolute;
    inset: 0;
    width: 1200px;
    height: 702px;
  }
  .company-name {
    position: absolute;
    left: 0;
    top: 58px;
    width: 1200px;
    margin: 0;
    text-align: center;
    font-size: 65px;
    font-weight: 400;
    line-height: 92px;
    letter-spacing: 0.5px;
    text-shadow: 0 2px 3px rgba(0,0,0,0.55);
  }
  .owner-line {
    position: absolute;
    left: 0;
    top: 167px;
    width: 1200px;
    margin: 0;
    text-align: center;
    font-size: 32px;
    font-weight: 400;
    color: var(--ink-soft);
  }
  .contact-list {
    position: absolute;
    left: 536px;
    top: 402px;
    margin: 0;
    padding: 0;
    list-style: none;
  }
  .contact-item {
    font-size: 29px;
    line-height: 40px;
    height: 40px;
    margin-bottom: 25px;
    white-space: nowrap;
  }
  .contact-item.email {
    font-size: 26px;
  }
  .contact-item.website {
    font-size: 25px;
    margin-left: 3px;
  }
</style>
</head>
<body>
  <div class="card">
    <svg class="card-backdrop" viewBox="0 0 1200 702" aria-hidden="true">
      <defs>
        <linearGradient id="base-shade" x1="0" y1="0" x2="0" y2="1">
          <stop offset="0" stop-color="#1c1d21"/>
          <stop offset="0.3" stop-color="#3a3b41"/>
          <stop offset="0.55" stop-color="#1e1f23"/>
          <stop offset="1" stop-color="#0b0c0e"/>
        </linearGradient>
        <radialGradient id="top-glow" cx="0.5" cy="0.3" r="0.55">
          <stop offset="0" stop-color="var(--card-glow)" stop-opacity="0.9"/>
          <stop offset="1" stop-color="var(--card-glow)" stop-opacity="0"/>
        </radialGradient>
        <linearGradient id="band-shade" x1="0" y1="0" x2="0" y2="1">
          <stop offset="0" stop-color="#3b3c42"/>
          <stop offset="1" stop-color="#4a4b52"/>
        </linearGradient>
        <linearGradient id="wave-shade" x1="0" y1="0" x2="0" y2="1">
          <stop offset="0" stop-color="#16181a"/>
          <stop offset="1" stop-color="var(--wave-dark)"/>
        </linearGradient>
      </defs>
      <rect class="base" width="1200" height="702" fill="url(#base-shade)"/>
      <rect class="glow" width="1200" height="420" fill="url(#top-glow)"/>
      <rect class="title-band" x="0" y="56" width="1200" height="98" fill="url(#band-shade)" opacity="0.85"/>
      <line class="title-rule" x1="0" y1="55" x2="1200" y2="55" stroke="var(--rule)" stroke-width="3"/>
      <line class="title-rule" x1="0" y1="155" x2="1200" y2="155" stroke="var(--rule)" stroke-width="3"/>
      <path class="wave" d="M60 702 C110 520 200 380 360 320 C470 282 600 290 760 302 C920 316 1060 326 1200 326 L1200 702 Z" fill="url(#wave-shade)"/>
    </svg>

    <h1 class="company-name">Brightwater Cleaning Service,LLC</h1>
    <p class="owner-line">Marco Villanueva Owner</p>

    <ul class="contact-list">
      <li class="contact-item email">Email: marco@brightwatercleaningservice.example</li>
      <li class="contact-item cell">Cell: 555-318-7724</li>
      <li class="contact-item office">Office: 555-374-6082</li>
      <li class="contact-item website">Website: www.brightwatercleaningservice.example</li>
    </ul>
  </div>
</body>
</html>
```